Local Construction Safety company needs advertising material

We need a brochure or flyer for a new company based in florida called Brightmoor Crest Services. We create safety solutions for residential construction sites. We are currently installing Ledge Rovers (Hanging Scaffolding system) for clients.

Colors:
Gold/Yellow
White
Light Grey
Dark Grey

Benefits to using us:

Exceeds NWSB requirements
Eliminates exposure to NWSB violations
Reduces the risk of fatal falls
Less accidents = Lower insurance rates
20% increase in efficiency
Structural integrity of dwelling isn’t compromised with this product
Cost is .2% of price of home
Happier framing crews

Target Market(s)

Custom home builders
Framing Comapnies
Shell Contractors

Industry/Entity Type

Residential Construction

Font styles to use
Serif

Colors
ffcf3e
aaaaaa
ffffff
dcdcdc

Requirements
Must have
• Benefits of service picture of product
• WHAT YOU CAN EXPECT:
• Innovative Solutions - Creative need-based solutions tailored to your safety goals
• On time service - Meeting or exceeding your construction scheduling needs
• Professionalism - Efficient, knowledgeable and friendly service
Should not have
• cheesy looking people

```html
<!DOCTYPE html>
<html lang="en">
<head>
<meta charset="utf-8">
<title>Brightmoor Crest Services – Flyer</title>
<link rel="stylesheet" href="https://fonts.googleapis.com/css2?family=Anton&family=Montserrat:ital,wght@0,600;0,700;0,800;1,500;1,600&display=swap">
<style>
  :root{
    --gold:#ffcf3e;
    --gold-deep:#f2b51c;
    --white:#ffffff;
    --light-grey:#dcdcdc;
    --mid-grey:#aaaaaa;
    --dark-grey:#3a3a3a;
    --charcoal:#262626;
    --sky-top:#4f86c6;
    --sky-low:#b9cfe2;
    --block:#cfcbc2;
    --ground:#8b7760;
  }
  *{margin:0;padding:0;box-sizing:border-box}
  html,body{width:848px;height:1200px;overflow:hidden;background:var(--white)}
  .flyer{position:relative;width:848px;height:1200px;overflow:hidden;font-family:"Montserrat",sans-serif;background:var(--charcoal)}
  .site-photo{position:absolute;left:0;top:0;width:848px;height:620px;
    background:linear-gradient(180deg,var(--sky-top) 0%,var(--sky-low) 30%,var(--block) 48%,var(--block) 68%,var(--ground) 100%)}
  .swoosh{position:absolute;left:0;top:0;width:848px;height:1200px}
  .brand{position:absolute;left:42px;top:66px;display:flex;align-items:center;gap:16px}
  .brand-mark{width:58px;height:58px;border:5px solid var(--gold)}
  .brand-name{font-family:"Montserrat",sans-serif;font-weight:800;font-size:27px;line-height:1.1;color:var(--gold);text-transform:uppercase;letter-spacing:1px;width:250px}
  .cert-badge{position:absolute;left:600px;top:350px;width:170px;height:170px;border-radius:50%;background:var(--white);display:flex;align-items:center;justify-content:center}
  .cert-badge span{display:block;width:136px;height:136px;border-radius:50%;background:var(--gold)}
  .benefits-title{position:absolute;top:640px;width:100%;text-align:center;font-family:"Anton",sans-serif;font-size:54px;letter-spacing:1px;color:var(--white)}
  .benefits-title em{font-style:normal;color:var(--gold)}
  .rule{position:absolute;left:166px;width:516px;height:2px;background:var(--gold)}
  .rule.top{top:713px}
  .rule.bottom{top:914px}
  .benefit-list{position:absolute;top:735px;left:34px;width:780px;display:flex;justify-content:space-between;list-style:none}
  .benefit{width:150px;text-align:center}
  .benefit svg{width:68px;height:68px;display:block;margin:0 auto 18px}
  .benefit p{font-weight:700;font-size:16px;line-height:1.25;color:var(--white);text-transform:uppercase}
  .insurance{position:absolute;top:926px;width:100%;text-align:center;font-style:italic;font-weight:500;font-size:21px;color:var(--white);text-transform:uppercase}
  .insurance strong{font-style:normal;font-weight:800;color:var(--gold)}
  .expect{position:absolute;left:0;top:970px;width:848px;height:230px;background:linear-gradient(135deg,var(--gold) 0%,var(--gold-deep) 100%)}
  .expect h2{position:absolute;left:30px;top:8px;font-family:"Anton",sans-serif;font-weight:400;font-size:46px;color:var(--white);letter-spacing:1px}
  .expect h2 span{color:var(--charcoal)}
  .expect-list{position:absolute;left:34px;top:80px;list-style:none}
  .expect-list li{display:flex;align-items:center;gap:14px;height:38px;font-size:17.5px;color:var(--charcoal)}
  .expect-list svg{width:22px;height:22px;flex:none}
  .expect-list strong{font-weight:800;text-transform:uppercase}
  .expect-list em{font-weight:500}
</style>
</head>
<body>
<main class="flyer">
  <div class="site-photo" role="img" aria-label="Photo of a residential concrete block house under construction with the hanging scaffolding system installed on its walls"></div>

  <svg class="swoosh" viewBox="0 0 848 1200" aria-hidden="true">
    <path d="M0,600 C260,640 560,590 848,330 L848,980 L0,980 Z" fill="var(--charcoal)"/>
    <path d="M0,560 C260,610 560,560 848,300 L848,360 C570,600 260,650 0,610 Z" fill="var(--gold)"/>
    <path d="M0,520 C260,575 560,530 848,270 L848,292 C560,550 260,595 0,545 Z" fill="var(--white)"/>
    <path d="M0,630 C260,665 560,615 848,360 L848,380 C560,635 260,685 0,650 Z" fill="var(--dark-grey)"/>
  </svg>

  <div class="brand">
    <div class="brand-mark"></div>
    <div class="brand-name">Brightmoor Crest Services</div>
  </div>

  <div class="cert-badge" aria-label="NWSB certified"><span></span></div>

  <h1 class="benefits-title">BENEFITS <em>TO USING US:</em></h1>
  <div class="rule top"></div>

  <ul class="benefit-list">
    <li class="benefit">
      <svg viewBox="0 0 68 68"><path d="M34 6 L64 60 H4 Z" fill="none" stroke="var(--gold)" stroke-width="5" stroke-linejoin="round"/><rect x="31" y="24" width="6" height="20" rx="2" fill="var(--gold)"/><circle cx="34" cy="51" r="3.5" fill="var(--gold)"/></svg>
      <p>Reduces the risk of fatal falls</p>
    </li>
    <li class="benefit">
      <svg viewBox="0 0 68 68"><circle cx="22" cy="12" r="6" fill="var(--gold)"/><path d="M26 22 L40 34 L54 30 M32 28 L24 48 L10 52 M40 34 L38 56" fill="none" stroke="var(--gold)" stroke-width="5" stroke-linecap="round"/><path d="M30 62 H62" stroke="var(--gold)" stroke-width="4" stroke-linecap="round"/></svg>
      <p>Reduces the risk of trip hazards</p>
    </li>
    <li class="benefit">
      <svg viewBox="0 0 68 68"><rect x="8" y="46" width="9" height="16" fill="var(--gold)"/><rect x="21" y="38" width="9" height="24" fill="var(--gold)"/><rect x="34" y="28" width="9" height="34" fill="var(--gold)"/><rect x="47" y="18" width="9" height="44" fill="var(--gold)"/><path d="M6 36 L30 14 L40 20 L58 6 M50 6 H58 V14" fill="none" stroke="var(--gold)" stroke-width="3" stroke-linecap="round"/></svg>
      <p>20% increase in efficiency</p>
    </li>
    <li class="benefit">
      <svg viewBox="0 0 68 68"><path d="M46 18 C42 12 22 10 22 22 C22 34 46 30 46 44 C46 56 24 56 20 48 M34 6 V62" fill="none" stroke="var(--gold)" stroke-width="6" stroke-linecap="round"/></svg>
      <p>Cost is .2% of price of home</p>
    </li>
    <li class="benefit">
      <svg viewBox="0 0 68 68"><circle cx="34" cy="34" r="28" fill="none" stroke="var(--gold)" stroke-width="4"/><path d="M22 35 L31 44 L47 26" fill="none" stroke="var(--gold)" stroke-width="5" stroke-linecap="round" stroke-linejoin="round"/></svg>
      <p>Happier framing crews</p>
    </li>
  </ul>

  <div class="rule bottom"></div>
  <p class="insurance">Less accidents <strong>= Lower insurance rates</strong></p>

  <section class="expect">
    <h2><span>WHAT YOU</span> CAN EXPECT:</h2>
    <ul class="expect-list">
      <li><svg viewBox="0 0 22 22"><circle cx="11" cy="11" r="10" fill="var(--white)"/><path d="M6 11 L10 15 L16 7" fill="none" stroke="var(--gold-deep)" stroke-width="2.5" stroke-linecap="round"/></svg><span><strong>Innovative Solutions -</strong> <em>Creative need-based solutions tailored to your safety goals</em></span></li>
      <li><svg viewBox="0 0 22 22"><circle cx="11" cy="11" r="10" fill="var(--white)"/><path d="M6 11 L10 15 L16 7" fill="none" stroke="var(--gold-deep)" stroke-width="2.5" stroke-linecap="round"/></svg><span><strong>On Time Service -</strong> <em>Meeting or exceeding your construction scheduling needs</em></span></li>
      <li><svg viewBox="0 0 22 22"><circle cx="11" cy="11" r="10" fill="var(--white)"/><path d="M6 11 L10 15 L16 7" fill="none" stroke="var(--gold-deep)" stroke-width="2.5" stroke-linecap="round"/></svg><span><strong>Professionalism -</strong> <em>Efficient, knowledgeable and friendly service</em></span></li>
    </ul>
  </section>
</main>
</body>
</html>
```